Coffee Package Design

We need a new package design for a coffee company. Need to be a mix between modern and classic design combined together. We are open to different ideas.
We changing our product name from Café Verlano to Café Brisota. The picture upload
shows what the product looks like. We want something completely different. The name of the company should go on the back of the package.
Updates

Hello Everyone,

Please read description, we are going with a new name and design for the product.

Café Brisota. Café Verlano is what we are replacing with Café Brisota, we are looking for new

look and design, please submit new designs.

There is a change in the description. Please take out Premium coffee blend and replace with Italian Roast.                                    

Industry/Entity Type

Cafe

Requirements
Must have
• You can use up to 6 colors.
Please put these items on design: Café Brisota (this is the product name), Regular Premium Blend Coffee, 100% Arabica,
Dulmore & Sons (name of the company), Tyler, TX on the back of the package

The file uploaded is an example of one of our products and how the package film
is sized.

```html
<!DOCTYPE html>
<html lang="en">
<head>
<meta charset="utf-8">
<title>Café Brisota – Regular Package Film</title>
<link rel="stylesheet" href="https://fonts.googleapis.com/css2?family=Roboto+Condensed:wght@700&display=swap">
<style>
  :root {
    --film-black: #050505;
    --gold: #ecca8c;
    --copper: #b8712c;
    --copper-deep: #8a4f1c;
    --page: #ffffff;
  }
  * { margin: 0; padding: 0; box-sizing: border-box; }
  html, body {
    width: 1200px;
    height: 1000px;
    overflow: hidden;
    background: var(--page);
  }
  .canvas {
    position: relative;
    width: 1200px;
    height: 1000px;
  }
  .film {
    position: absolute;
    left: 39px;
    top: 146px;
    width: 748px;
    height: 472px;
    background: var(--film-black);
    transform: scale(1.5);
    transform-origin: top left;
    overflow: hidden;
    font-family: "Roboto Condensed", sans-serif;
    font-weight: 700;
    font-style: normal;
  }
  .fold-line {
    position: absolute;
    top: 0;
    bottom: 0;
    width: 1px;
    background: var(--copper-deep);
  }
  .fold-line--a { left: 69px; }
  .fold-line--b { left: 224px; }
  .fold-line--c { left: 592px; }

  .brand-name {
    font-family: "Roboto Condensed", sans-serif;
    font-weight: 700;
    color: var(--gold);
    text-transform: uppercase;
    line-height: 0.95;
    letter-spacing: 0;
  }
  .brand-name__cafe,
  .brand-name__main { display: block; }

  .front-label {
    position: absolute;
    left: 224px;
    width: 368px;
    top: 96px;
    text-align: center;
  }
  .front-label .brand-name__cafe { font-size: 56px; }
  .front-label .brand-name__main { font-size: 72px; }
  .roast {
    font-size: 21px;
    color: var(--copper);
    margin-top: 8px;
  }
  .origin {
    font-size: 13px;
    color: var(--gold);
    margin-top: 52px;
  }

  .side-mark {
    position: absolute;
    left: 146px;
    top: 236px;
    transform: translate(-50%, -50%) rotate(-90deg);
    white-space: nowrap;
    display: flex;
    align-items: flex-end;
    gap: 6px;
  }
  .side-mark .brand-name__cafe { font-size: 22px; }
  .side-mark .brand-name__main { font-size: 34px; }
  .side-mark__tag {
    display: flex;
    flex-direction: column;
    line-height: 1;
    color: var(--copper);
    padding-bottom: 4px;
  }
  .side-mark__tag-title { font-size: 12px; }
  .side-mark__tag-sub { font-size: 7px; }

  .maker {
    position: absolute;
    left: 672px;
    top: 222px;
    transform: translate(-50%, -50%) rotate(-90deg);
    white-space: nowrap;
    text-align: center;
    font-style: normal;
    font-size: 14px;
    line-height: 1.25;
    color: var(--gold);
  }
</style>
</head>
<body>
<main class="canvas">
  <section class="film" aria-label="Café Brisota Regular package film">
    <div class="fold-line fold-line--a"></div>
    <div class="fold-line fold-line--b"></div>
    <div class="fold-line fold-line--c"></div>

    <div class="side-mark">
      <div class="brand-name">
        <span class="brand-name__cafe">Café</span>
        <span class="brand-name__main">Brisota</span>
      </div>
      <div class="side-mark__tag">
        <span class="side-mark__tag-title">Premium</span>
        <span class="side-mark__tag-sub">Blend Coffee</span>
      </div>
    </div>

    <div class="front-label">
      <h1 class="brand-name">
        <span class="brand-name__cafe">Café</span>
        <span class="brand-name__main">Brisota</span>
      </h1>
      <p class="roast">Regular</p>
      <p class="origin">100% Arabica</p>
    </div>

    <address class="maker">
      Dulmore &amp; Sons<br>Oakvale, Texas
    </address>
  </section>
</main>
</body>
</html>
```